Small rum distillery looking for bottle design

Small rum distillery in Estonia. Looking for bottle lable design. It should be simple but at the same time point out from the variety of other bottles.
As we are a small nordic country, design can be some how nordic or represent our country. It can also have some connection with sailing or sea as we know it pirates love it.
Bottle we are using is Corvane 540

Industry/Entity Type

food and beverage

Other font styles liked:
• Baskerville

```html
<!DOCTYPE html>
<html lang="en">
<head>
<meta charset="utf-8">
<title>Halder Distillery – Rum Label</title>
<link href="https://fonts.googleapis.com/css2?family=EB+Garamond:ital,wght@0,400;0,500;1,400&display=swap" rel="stylesheet">
<style>
  :root {
    --backdrop: #000000;
    --glass-light: #ec7612;
    --glass-deep: #c24400;
    --glass-mid: #cc5d06;
    --glass-right: #d98a0a;
    --outline: #e8e8e8;
    --label-paper: #f5f6f0;
    --label-ornament: #ecede4;
    --ink-dark: #333333;
    --ink-grey: #555555;
    --ink-red: #b3232c;
  }
  html, body {
    margin: 0;
    padding: 0;
    width: 1200px;
    height: 1200px;
    overflow: hidden;
    background: var(--backdrop);
  }
  .bottle-canvas {
    display: block;
    width: 1200px;
    height: 1200px;
  }
  .label-type {
    font-family: "EB Garamond", "Libre Baskerville", serif;
  }
  .spirit-name { fill: var(--ink-red); font-style: italic; font-size: 32px; letter-spacing: 5px; }
  .brand-name { fill: var(--ink-dark); font-size: 64px; letter-spacing: 3px; }
  .brand-sub { fill: var(--ink-dark); font-size: 24px; letter-spacing: 5px; }
  .volume { fill: var(--ink-red); font-size: 23px; }
  .strength { fill: var(--ink-grey); font-size: 23px; }
  .strength-note { fill: var(--ink-grey); font-size: 12px; }
</style>
</head>
<body>
<svg class="bottle-canvas" viewBox="0 0 1200 1200" xmlns="http://www.w3.org/2000/svg">
  <defs>
    <linearGradient id="glassTone" x1="0" y1="0" x2="1" y2="0">
      <stop offset="0" stop-color="var(--glass-light)"/>
      <stop offset="0.28" stop-color="var(--glass-deep)"/>
      <stop offset="0.6" stop-color="var(--glass-mid)"/>
      <stop offset="1" stop-color="var(--glass-right)"/>
    </linearGradient>
  </defs>

  <!-- bottle outline -->
  <path class="bottle-outline"
        d="M522 134 H680 V352 C680 378 720 384 752 398 C790 416 808 450 808 495 V1050 Q808 1068 790 1068 H412 Q394 1068 394 1050 V495 C394 450 412 416 450 398 C482 384 522 378 522 352 Z"
        fill="none" stroke="var(--outline)" stroke-width="2"/>

  <!-- bottle glass -->
  <path class="bottle-glass"
        d="M527 140 H675 V352 C675 382 714 388 748 402 C785 420 803 452 803 497 V1048 Q803 1062 789 1062 H413 Q399 1062 399 1048 V497 C399 452 417 420 454 402 C488 388 527 382 527 352 Z"
        fill="url(#glassTone)"/>

  <!-- glass highlights -->
  <rect class="glass-highlight" x="562" y="200" width="18" height="225" rx="5" fill="#ffffff" opacity="0.55"/>
  <path class="glass-highlight" d="M430 430 C450 405 480 395 510 390 L505 410 C480 418 455 430 445 448 Z" fill="#ffffff" opacity="0.35"/>
  <rect class="glass-highlight" x="424" y="450" width="22" height="582" rx="8" fill="#ffffff" opacity="0.6"/>

  <!-- label -->
  <path class="label-paper"
        d="M600 487 C625 510 660 528 700 548 L750 572 C742 590 760 600 795 610 V880 C760 890 742 900 752 920 L700 940 C660 958 625 975 600 998 C575 975 540 958 500 940 L448 920 C458 900 440 890 407 880 V610 C440 600 458 590 450 572 L500 548 C540 528 575 510 600 487 Z"
        fill="var(--label-paper)"/>
  <circle class="label-ornament" cx="600" cy="742" r="170" fill="var(--label-ornament)"
          role="img" aria-label="faint interlaced knot ornament behind the label text"/>

  <g class="label-type">
    <text class="spirit-name" x="600" y="580" text-anchor="middle">rum</text>
    <rect class="brand-marker" x="582" y="636" width="36" height="36" fill="var(--ink-red)"/>
    <text class="brand-name" x="600" y="786" text-anchor="middle">HALDER</text>
    <line class="brand-rule" x1="470" y1="802" x2="730" y2="802" stroke="var(--ink-dark)" stroke-width="2"/>
    <text class="brand-sub" x="603" y="836" text-anchor="middle">DISTILLERY</text>
    <text class="volume" x="600" y="894" text-anchor="middle">700ml</text>
    <text class="strength" x="600" y="933" text-anchor="middle">40%</text>
    <text class="strength-note" x="600" y="950" text-anchor="middle">alc. by vol.</text>
  </g>
</svg>
</body>
</html>
```